Business Card Design Project

Industry/Entity Type

Business

Contact Information for Business Card

The Harlow Vale Gospel Choir
Dean Marsell, Minister of Music

The Coastal Wesleyan Church of Bramford Hill
Founded 1792

Twitter @thehvgc
Instagram harlowvalegc
Facebook facebook.com/hvgc408
Website: harlowvalegc-example.org
For Bookings: (555) 204-HVGC
4287 Bramwell Street, Philadelphia, PA 19874

Back of the Card
Music and Cd's Recordings Available On
Choirs Website and Also
Tunevox, Orbala Sound, Disc Sprout (the music online logo)

```html
<!DOCTYPE html>
<html lang="en">
<head>
<meta charset="utf-8">
<title>The Harlow Vale Gospel Choir Business Card</title>
<link href="https://fonts.googleapis.com/css2?family=Roboto:wght@300;400;700;900&display=swap" rel="stylesheet">
<style>
  :root {
    --stage: #dcdcde;
    --card-white: #ffffff;
    --card-black: #2b2b2d;
    --brand-red: #d4161b;
    --ink: #333333;
    --ink-soft: #666666;
    --ink-light: #d9d9d9;
    --pill-line: #6a6a6c;
  }
  * { box-sizing: border-box; margin: 0; padding: 0; }
  html, body {
    width: 1200px; height: 799px; overflow: hidden;
    background: var(--stage);
    font-family: "Roboto", Arial, sans-serif;
  }
  .stage {
    width: 1200px; height: 799px;
    display: flex; align-items: center; justify-content: center; gap: 60px;
  }
  .card {
    position: relative; width: 520px; height: 300px;
    border-radius: 18px; overflow: hidden;
    box-shadow: 0 6px 18px rgba(0,0,0,0.18);
  }
  .card--front { background: var(--card-white); }
  .card--back { background: var(--card-black); }

  .drip-area { position: absolute; top: 0; left: 0; width: 520px; height: 300px; }

  .contact-list {
    position: absolute; left: 34px; top: 32px; width: 230px;
    list-style: none; display: flex; flex-direction: column; gap: 11px;
  }
  .contact-item { display: flex; align-items: flex-start; gap: 10px; }
  .contact-icon {
    width: 20px; height: 20px; flex: none; border-radius: 3px;
    background: var(--brand-red); display: flex; align-items: center; justify-content: center;
  }
  .contact-text { font-size: 10.5px; line-height: 14px; color: var(--ink-soft); }
  .contact-label { font-weight: 700; color: var(--ink); }
  .contact-name { font-weight: 700; color: var(--ink); text-transform: uppercase; font-size: 11.5px; }

  .brand { position: absolute; display: flex; align-items: center; gap: 10px; }
  .brand-mark { width: 30px; height: 30px; border-radius: 50%; background: var(--brand-red); flex: none; }
  .brand-name {
    font-weight: 900; font-size: 14px; letter-spacing: 0.4px;
    text-transform: uppercase; line-height: 1.15;
  }
  .brand-tagline { font-weight: 400; font-size: 8.5px; letter-spacing: 0.4px; line-height: 12px; margin-top: 4px; }
  .card--front .brand { left: 276px; top: 200px; width: 220px; }
  .card--front .brand-name { color: var(--ink); }
  .card--front .brand-tagline { color: var(--ink-soft); }

  .back-content {
    position: absolute; left: 0; top: 62px; width: 520px;
    display: flex; flex-direction: column; align-items: center;
  }
  .card--back .brand { position: static; }
  .card--back .brand-name { color: var(--card-white); }
  .card--back .brand-tagline { color: var(--ink-light); }

  .availability {
    margin-top: 22px; font-size: 10px; letter-spacing: 0.6px;
    color: var(--ink-light); text-transform: uppercase; text-align: center; line-height: 14px;
  }
  .platforms { display: flex; gap: 18px; margin-top: 10px; list-style: none; }
  .platform {
    display: flex; align-items: center; gap: 6px;
    font-size: 11px; font-weight: 700; color: var(--card-white);
  }
  .platform-dot { width: 8px; height: 8px; border-radius: 50%; background: var(--brand-red); }

  .web-pill {
    margin-top: 16px; height: 24px; padding: 0 14px 0 10px;
    border: 1px solid var(--pill-line); border-radius: 12px;
    display: flex; align-items: center; gap: 7px;
    font-size: 9.5px; color: var(--ink-light);
  }
</style>
</head>
<body>
<main class="stage">

  <section class="card card--front" aria-label="Card front">
    <svg class="drip-area" viewBox="0 0 520 300" role="img" aria-label="Red paint drip decoration along the top right edge">
      <path fill="var(--brand-red)" d="M250 0 H520 V175 C505 168 500 140 488 132 C470 120 458 112 445 102 C428 88 412 74 392 68 C365 58 340 46 318 34 C295 22 272 12 250 0 Z"/>
    </svg>

    <ul class="contact-list">
      <li class="contact-item">
        <span class="contact-icon"><svg width="12" height="12" viewBox="0 0 12 12"><circle cx="6" cy="4" r="2.5" fill="#fff"/><path d="M1.5 11.5 C1.5 8 10.5 8 10.5 11.5 Z" fill="#fff"/></svg></span>
        <p class="contact-text"><span class="contact-name">Dean Marsell</span><br>Minister of Music</p>
      </li>
      <li class="contact-item">
        <span class="contact-icon"><svg width="12" height="12" viewBox="0 0 12 12"><path d="M2.5 1 L4.5 1 L5.2 3.6 L4 4.6 C4.6 6 6 7.4 7.4 8 L8.4 6.8 L11 7.5 L11 9.5 C11 10.4 10.4 11 9.5 11 C5 11 1 7 1 2.5 C1 1.6 1.6 1 2.5 1 Z" fill="#fff"/></svg></span>
        <p class="contact-text"><span class="contact-label">For Bookings</span><br>(555) 204-HVGC</p>
      </li>
      <li class="contact-item">
        <span class="contact-icon"><svg width="12" height="12" viewBox="0 0 12 12"><circle cx="6" cy="6" r="4.6" fill="none" stroke="#fff" stroke-width="1"/><path d="M1.4 6 H10.6 M6 1.4 C3.8 3.6 3.8 8.4 6 10.6 M6 1.4 C8.2 3.6 8.2 8.4 6 10.6" fill="none" stroke="#fff" stroke-width="0.9"/></svg></span>
        <p class="contact-text"><span class="contact-label">Website</span><br>harlowvalegc-example.org</p>
      </li>
      <li class="contact-item">
        <span class="contact-icon"><svg width="12" height="12" viewBox="0 0 12 12"><circle cx="3" cy="6" r="1.6" fill="#fff"/><circle cx="9" cy="2.8" r="1.6" fill="#fff"/><circle cx="9" cy="9.2" r="1.6" fill="#fff"/><path d="M3 6 L9 2.8 M3 6 L9 9.2" stroke="#fff" stroke-width="1"/></svg></span>
        <p class="contact-text">Twitter @thehvgc<br>Instagram harlowvalegc<br>facebook.com/hvgc408</p>
      </li>
      <li class="contact-item">
        <span class="contact-icon"><svg width="12" height="12" viewBox="0 0 12 12"><path d="M6 11.5 C3 8 2 6 2 4.5 A4 4 0 0 1 10 4.5 C10 6 9 8 6 11.5 Z" fill="#fff"/><circle cx="6" cy="4.5" r="1.5" fill="var(--brand-red)"/></svg></span>
        <p class="contact-text">4287 Bramwell Street<br>Philadelphia, PA 19874</p>
      </li>
    </ul>

    <div class="brand">
      <span class="brand-mark"></span>
      <div>
        <p class="brand-name">The Harlow Vale Gospel Choir</p>
        <p class="brand-tagline">The Coastal Wesleyan Church of Bramford Hill<br>Founded 1792</p>
      </div>
    </div>
  </section>

  <section class="card card--back" aria-label="Card back">
    <svg class="drip-area" viewBox="0 0 520 300" role="img" aria-label="Red paint drip decoration along the top right edge">
      <path fill="var(--brand-red)" d="M300 0 H520 V100 C505 96 495 82 482 74 C465 62 448 54 430 46 C405 36 380 28 355 20 C335 14 318 8 300 0 Z"/>
    </svg>

    <div class="back-content">
      <div class="brand">
        <span class="brand-mark"></span>
        <div>
          <p class="brand-name">The Harlow Vale Gospel Choir</p>
          <p class="brand-tagline">The Coastal Wesleyan Church of Bramford Hill</p>
        </div>
      </div>

      <p class="availability">Music and CD recordings available on<br>the choir's website and also</p>

      <ul class="platforms">
        <li class="platform"><span class="platform-dot"></span>Tunevox</li>
        <li class="platform"><span class="platform-dot"></span>Orbala Sound</li>
        <li class="platform"><span class="platform-dot"></span>Disc Sprout</li>
      </ul>

      <p class="web-pill">
        <svg width="10" height="10" viewBox="0 0 10 10"><circle cx="5" cy="5" r="4.2" fill="none" stroke="var(--ink-light)" stroke-width="0.9"/><path d="M0.8 5 H9.2 M5 0.8 C3 3 3 7 5 9.2 M5 0.8 C7 3 7 7 5 9.2" fill="none" stroke="var(--ink-light)" stroke-width="0.8"/></svg>
        harlowvalegc-example.org
      </p>
    </div>
  </section>

</main>
</body>
</html>
```